we can communicate on this, but i want to follow the approach we took on Pell|Quorn & Tillet but i feel the card front needs the black background and the platinum and gold logo. The back? I am open. we can use the same info from PQ&T. Vellum Crest is an enhanced equity investment fund - basically a very exclusive boutique hedge fund that uses only stock options. very advanced things. hope you are interested

Contact Information for Business Card

Dr. Owen T. Brisket, CFA
Scientifique de fusée financière
555.014.2296
TheDoc4793@mailvessel.example

4718 Fennel Brook Way N.
West Fargo, ND 58078

No web site

Colors

Designer to choose colors to be used in the design.

Requirements
Nice to have
• I tend to prefer the most visible applications of the logo to include logo and name, the logo version with a black background and the gold and platinum components separated by the black. I see this working well for a single side (logo and name - this is card front to me).
• I am fairly open to other treatments on the reverse side with the data. To me, it makes sense to have a different color rendition of the logo on the reverse and it may be a muted black tone on tone or an oversized portion that would have spot UV. Or, the reverse may play with colors and layout
Should not have
• Other colors = no no
• Decorative font

```html
<!DOCTYPE html>
<html lang="en">
<head>
<meta charset="utf-8">
<title>Vellum Crest — Business Card</title>
<link rel="stylesheet" href="https://fonts.googleapis.com/css2?family=Montserrat:wght@400;500;700&display=swap">
<style>
  :root {
    --stage: #161616;
    --card: #1f1f1f;
    --card-edge: #2a2a2a;
    --gold: #d4a82c;
    --platinum: #b9b9bb;
    --muted: #6f6f70;
    --ink: #f4f4f4;
  }
  * { margin: 0; padding: 0; box-sizing: border-box; }
  html, body {
    width: 1200px; height: 900px; overflow: hidden;
    background: var(--stage);
    font-family: "Montserrat", sans-serif;
  }
  .canvas {
    width: 1200px; height: 900px;
    display: flex; flex-direction: column; align-items: center; justify-content: center;
    gap: 36px;
  }
  .card {
    width: 700px; height: 400px;
    background: var(--card);
    border: 1px solid var(--card-edge);
    position: relative;
    box-shadow: 0 14px 30px rgba(0,0,0,.55);
  }

  /* Front */
  .card--front { display: flex; flex-direction: column; align-items: center; justify-content: center; }
  .brand-mark { border-radius: 50%; display: block; }
  .card--front .brand-mark { width: 96px; height: 96px; background: var(--muted); margin-bottom: 22px; }
  .brand-name {
    font-weight: 700; text-transform: uppercase; text-align: center;
    line-height: 1.1; white-space: nowrap;
  }
  .card--front .brand-name { color: var(--muted); font-size: 34px; letter-spacing: 3px; }

  /* Back */
  .card--back { display: flex; align-items: center; }
  .brand-block {
    width: 290px; display: flex; flex-direction: column; align-items: center;
  }
  .card--back .brand-mark { width: 104px; height: 104px; background: var(--gold); margin-bottom: 18px; }
  .card--back .brand-name { color: var(--ink); font-size: 28px; letter-spacing: 1.5px; }
  .divider { width: 2px; height: 200px; background: var(--gold); flex: none; }
  .contact { padding-left: 36px; padding-right: 20px; color: var(--ink); }
  .contact__name {
    color: var(--gold); font-weight: 700; font-size: 18px; letter-spacing: 1px;
    text-transform: uppercase; white-space: nowrap;
  }
  .contact__title { font-size: 15px; font-weight: 500; margin: 2px 0 16px; letter-spacing: .3px; }
  .contact__address { font-size: 16px; line-height: 1.4; letter-spacing: .4px; margin-bottom: 12px; }
  .contact__list { list-style: none; font-size: 16px; line-height: 1.6; letter-spacing: .4px; }
  .contact__list li { display: flex; align-items: center; gap: 10px; white-space: nowrap; }
  .contact__icon { width: 14px; height: 14px; flex: none; }
</style>
</head>
<body>
<main class="canvas">

  <section class="card card--front" aria-label="Card front">
    <span class="brand-mark"></span>
    <div class="brand-name">Vellum Crest</div>
  </section>

  <section class="card card--back" aria-label="Card back">
    <div class="brand-block">
      <span class="brand-mark"></span>
      <div class="brand-name">Vellum Crest</div>
    </div>
    <div class="divider"></div>
    <div class="contact">
      <div class="contact__name">Dr. Owen T. Brisket, CFA</div>
      <div class="contact__title">Scientifique de fusée financière</div>
      <div class="contact__address">4718 Fennel Brook Way N.<br>West Fargo, ND 58078</div>
      <ul class="contact__list">
        <li>
          <svg class="contact__icon" viewBox="0 0 16 16" aria-hidden="true">
            <path d="M4 1.5 L6.2 4.5 L4.8 6 C5.6 8 7.8 10.3 10 11.2 L11.5 9.8 L14.5 12 L12.8 14.4 C7.5 14 2 8.5 1.6 3.2 Z" fill="var(--gold)"/>
          </svg>
          555.014.2296
        </li>
        <li>
          <svg class="contact__icon" viewBox="0 0 16 16" aria-hidden="true">
            <rect x="1.5" y="3.5" width="13" height="9" fill="none" stroke="var(--gold)" stroke-width="1.5"/>
            <path d="M1.5 3.5 L8 9 L14.5 3.5" fill="none" stroke="var(--gold)" stroke-width="1.5"/>
          </svg>
          TheDoc4793@mailvessel.example
        </li>
      </ul>
    </div>
  </section>

</main>
</body>
</html>
```